International Food Manufacturer in the need of a new business card and logo.

Our Company - Northgate Pantry Ltd.

Our Industry - Food and Drink

We are a Wild Harvested Food Distributor / Manufacturer. We service the following food sectors: Supermarkets, Hotels, Restaurants, Cafes, Catering and all people looking to eat healthy food products.

Slogan - The foremost source for everything healthy

Business card details -

48-52 Marlow Lane
Hatherby Green
London
EC9Z 4RT United Kingdom
Dennis Prowle
+44 7000 481736 - UK
+971 50 7739205 - UAE
+38 063 914 2758 - Ukraine
dennis@northgatepantry.example
www.northgatepantry.example

Goal - We are looking for a dynamic modern new look for our corporate image and a designer who can bring this new concept to our future food product designs. Please try to incorporate 3d hexagonal vector Imaging in your design concepts.

Target Market(s)

Industry/Entity Type

Food Service

Contact Information for Business Card

Northgate Pantry Ltd.
48-52 Marlow Lane
Hatherby Green
London
EC9Z 4RT United Kingdom
Dennis Prowle
+44 7000 481736 - UK
+971 50 7739205 - UAE

Font styles to use
Serif

Colors

Designer to choose colors to be used in the design.

Requirements
Must have
• Please read project description above.
Nice to have
Should not have

```html
<!DOCTYPE html>
<html lang="en">
<head>
<meta charset="utf-8">
<title>Northgate Pantry Ltd. – Banner</title>
<link rel="stylesheet" href="https://fonts.googleapis.com/css2?family=Signika:wght@500;600;700&display=swap">
<style>
  :root {
    --backdrop: #bbbcbe;
    --paper: #ffffff;
    --brand-red: #e31e24;
    --band-red-top: #ee1c25;
    --band-red-bottom: #c8101a;
    --ink: #111111;
    --on-red: #ffffff;
  }
  * { margin: 0; padding: 0; box-sizing: border-box; }
  html, body { width: 1200px; height: 1200px; overflow: hidden; }
  body {
    background: var(--backdrop);
    font-family: "Signika", "Trebuchet MS", sans-serif;
    position: relative;
  }
  .banner {
    position: absolute;
    left: 44px; top: 283px;
    width: 1108px; height: 632px;
    background: var(--paper);
    overflow: hidden;
  }
  .banner-art { position: absolute; inset: 0; width: 100%; height: 100%; }
  .company-name {
    position: absolute; left: 0; right: 0; top: 30px;
    display: flex; justify-content: center; align-items: center; gap: 10px;
    color: var(--brand-red);
    font-weight: 600; font-size: 22px; line-height: 24px;
  }
  .company-mark {
    width: 16px; height: 16px; border-radius: 50%;
    background: var(--brand-red);
  }
  .headline {
    position: absolute; left: 0; right: 0;
    text-align: center;
    color: var(--brand-red);
    font-weight: 600;
    line-height: 1;
    white-space: nowrap;
  }
  .headline--top { top: 90px; font-size: 70px; }
  .headline--bottom { top: 152px; font-size: 73px; letter-spacing: 0.5px; }
  .sectors-title {
    position: absolute; left: 0; right: 0; top: 243px;
    text-align: center; color: var(--ink);
    font-weight: 600; font-size: 21px; line-height: 22px;
  }
  .sectors-list {
    position: absolute; left: 0; right: 0; top: 274px;
    text-align: center; color: var(--brand-red);
    font-weight: 600; font-size: 21px; line-height: 27px;
  }
  .contact {
    position: absolute; color: var(--on-red);
    font-weight: 600; white-space: nowrap;
  }
  .contact svg { position: absolute; }
  .address-line-1 { left: 0; right: 0; top: 433px; height: 26px; font-size: 20px; line-height: 26px; }
  .address-line-2 { left: 0; right: 0; top: 459px; text-align: center; font-size: 20px; line-height: 26px; }
  .address-line-1 span { position: absolute; left: 281px; }
  .phone-row, .web-row { left: 0; right: 0; height: 24px; font-size: 22px; line-height: 24px; }
  .phone-row { top: 510px; }
  .web-row { top: 565px; }
  .phone-row span, .web-row span { position: absolute; }
</style>
</head>
<body>
  <section class="banner">
    <svg class="banner-art" viewBox="0 0 1385 791" preserveAspectRatio="none">
      <defs>
        <linearGradient id="bandRed" x1="0" y1="0" x2="0" y2="1">
          <stop offset="0" stop-color="#ee1c25"/>
          <stop offset="1" stop-color="#c8101a"/>
        </linearGradient>
        <linearGradient id="produceFill" x1="0" y1="0" x2="1" y2="1">
          <stop offset="0" stop-color="#c9772f"/>
          <stop offset="0.55" stop-color="#a85a22"/>
          <stop offset="1" stop-color="#7da53a"/>
        </linearGradient>
        <linearGradient id="bottleFill" x1="0" y1="0" x2="1" y2="0">
          <stop offset="0" stop-color="#e6ddc8"/>
          <stop offset="0.5" stop-color="#c99a55"/>
          <stop offset="1" stop-color="#cfd6dc"/>
        </linearGradient>
      </defs>
      <path role="img" aria-label="Photograph of wicker baskets filled with fresh vegetables: carrots, cauliflower, cabbage, peppers and aubergine"
            d="M0,266 Q250,270 432,484 L432,700 L0,700 Z" fill="url(#produceFill)"/>
      <path role="img" aria-label="Photograph of an assortment of spirit and liqueur bottles"
            d="M955,486 Q1150,272 1385,266 L1385,700 L955,700 Z" fill="url(#bottleFill)"/>
      <path d="M0,266 Q250,270 432,484" fill="none" stroke="#e31e24" stroke-width="1.2"/>
      <path d="M955,486 Q1150,272 1385,266" fill="none" stroke="#e31e24" stroke-width="1.2"/>
      <path d="M0,636 Q692,286 1385,636 L1385,791 L0,791 Z" fill="url(#bandRed)"/>
    </svg>

    <div class="company-name"><span class="company-mark"></span><span>Northgate Pantry Ltd.</span></div>

    <div class="headline headline--top">The Foremost Source for</div>
    <div class="headline headline--bottom">EVERYTHING HEALTHY</div>

    <div class="sectors-title">Services the Food Sectors</div>
    <div class="sectors-list">Supermarkets, Hotels, Restaurants, Cafes, Catering<br>and all people looking to eat healthy food products</div>

    <div class="contact address-line-1">
      <svg width="38" height="38" viewBox="0 0 38 38" style="left:232px;top:-6px" aria-hidden="true">
        <circle cx="19" cy="19" r="19" fill="#fff"/>
        <path d="M8,19 L19,9 L30,19" fill="none" stroke="#e31e24" stroke-width="3" stroke-linejoin="round"/>
        <path d="M12,18 V29 H17 V23 H21 V29 H26 V18" fill="#e31e24"/>
      </svg>
      <span>48-52 Marlow Lane Hatherby Green London EC9Z 4RT</span>
    </div>
    <div class="contact address-line-2">United Kingdom&nbsp; Dennis Prowle</div>

    <div class="contact phone-row">
      <svg width="38" height="38" viewBox="0 0 38 38" style="left:143px;top:-8px" aria-hidden="true">
        <circle cx="19" cy="19" r="19" fill="#fff"/>
        <path d="M12,10 L16,10 L18,15 L15.5,17 Q17.5,21 21,22.5 L23,20 L28,22 L28,26 Q26,29 22,28 Q13,25 10,16 Q9,12 12,10 Z" fill="#e31e24"/>
      </svg>
      <span style="left:207px">UK +44 7000 481736</span>
      <span style="left:457px">UAE +971 50 7739205</span>
      <span style="left:708px">Ukraine +38 063 914 2758</span>
    </div>

    <div class="contact web-row">
      <svg width="38" height="38" viewBox="0 0 38 38" style="left:159px;top:-7px" aria-hidden="true">
        <circle cx="19" cy="19" r="19" fill="#fff"/>
        <rect x="9" y="12" width="20" height="14" rx="2" fill="none" stroke="#e31e24" stroke-width="2.4"/>
        <path d="M10,13 L19,20 L28,13" fill="none" stroke="#e31e24" stroke-width="2.4"/>
      </svg>
      <span style="left:212px">dennis@northgatepantry.example</span>
      <svg width="38" height="38" viewBox="0 0 38 38" style="left:584px;top:-7px" aria-hidden="true">
        <circle cx="19" cy="19" r="19" fill="#fff"/>
        <g fill="none" stroke="#e31e24" stroke-width="1.8">
          <circle cx="19" cy="19" r="11"/>
          <ellipse cx="19" cy="19" rx="5" ry="11"/>
          <path d="M8,19 H30 M10,13 H28 M10,25 H28 M19,8 V30"/>
        </g>
      </svg>
      <span style="left:638px">www.northgatepantry.example</span>
    </div>
  </section>
</body>
</html>
```